meridale partners business card

Architectural firm business card
Updates

Please note:

corporate colour black+yellow are the only elements to be kept.
NO OTHER ELEMENT TO BE REUSED FROM PREVIOUS BUSINESS CARD.
Thank you.

Dear Everyone,

Thank you for your participation. I have upload the KBSO+ logo again for incoporate in the card. in tif and pdf format.

Thank you 

I keep getting request for the logo file. Does everyone has the same problem?

I cannot do much, because the file is upload to the website server. I can't seem to see it either.

The logo file is now working. Please download. I check it myself. Thank you everyone.

Dear All,

Thank you for all the hard work. There are a lot of great work. Due to current commitment with work, I am unable to review them just yet. I will do so next week and advise everyone also. Thank you again. Best regards

Dear All,

Thank you for your participation. There are a lot of good design. Unfortunately, I can only select one. All the best. This is definitely a good crowd to work with. Thank you everyone again.

Best regards

Target Market(s)

Corporate, commercial and institutional projects only

Industry/Entity Type

Business

Requirements
Must have
• elegant simple
double sided with coating
Member of Southland Guild of Draughtsmen (logo only)
corporate colour black and

LOGO FILE UPLOADED
Should not have
• should not be the same as current business card.
upload for reference information only.
font sans serif preferred.

```html
<!DOCTYPE html>
<html lang="en">
<head>
<meta charset="utf-8">
<title>Meridale Partners – Business Card</title>
<link href="https://fonts.googleapis.com/css2?family=Open+Sans:wght@300;400;600;700&display=swap" rel="stylesheet">
<style>
  :root {
    --bg: #111111;
    --yellow: #f2d40f;
    --black: #1c1c1c;
    --ink: #232323;
    --ink-soft: #3a3a3a;
  }
  * { margin: 0; padding: 0; box-sizing: border-box; }
  html, body { width: 1200px; height: 1023px; overflow: hidden; background: var(--bg); }
  body { font-family: "Open Sans", Arial, sans-serif; position: relative; }

  .card {
    position: absolute;
    left: 290px;
    width: 620px;
    height: 370px;
    border-radius: 18px;
    overflow: hidden;
  }
  .card--front { top: 96px; background: var(--yellow); color: var(--ink); }
  .card--back  { top: 560px; background: var(--black); color: var(--yellow); }

  /* front */
  .brand {
    position: absolute; top: 36px; right: 40px;
    display: flex; align-items: center; gap: 12px;
  }
  .brand__mark { width: 22px; height: 22px; background: currentColor; }
  .brand__name { font-weight: 700; font-size: 22px; letter-spacing: 1px; line-height: 1; text-transform: uppercase; }
  .brand__sub  { display: block; font-weight: 700; font-size: 13px; letter-spacing: 1.5px; margin-top: 4px; }

  .contact {
    position: absolute; top: 112px; right: 40px;
    text-align: right; font-size: 12.5px; line-height: 1.65; color: var(--ink-soft);
  }
  .contact b { font-weight: 700; color: var(--ink); }
  .contact .web { font-weight: 700; color: var(--ink); }

  .membership {
    position: absolute; left: 40px; top: 120px;
    display: flex; align-items: center; gap: 12px;
  }
  .membership__badge { width: 64px; height: 64px; background: var(--ink); }
  .membership__text { font-size: 10px; line-height: 1.25; font-weight: 600; color: var(--ink); width: 110px; }

  .person { position: absolute; left: 40px; top: 206px; font-size: 12.5px; color: var(--ink-soft); line-height: 1.5; }
  .person__name { font-size: 19px; font-weight: 700; color: var(--ink); }
  .person__name small { font-size: 12px; font-weight: 600; }
  .person__role { font-weight: 700; color: var(--ink); font-size: 14px; margin-top: 6px; }

  .services-band {
    position: absolute; left: 0; right: 0; bottom: 0; height: 48px;
    background: var(--black); color: var(--yellow);
    display: flex; align-items: center; padding-left: 40px;
    font-size: 14px; letter-spacing: 3px; font-weight: 300;
  }

  /* back */
  .card--back .brand { position: absolute; top: 120px; left: 50%; right: auto; transform: translateX(-50%); gap: 16px; }
  .card--back .brand__mark { width: 34px; height: 34px; }
  .card--back .brand__name { font-size: 34px; }
  .card--back .brand__sub { font-size: 18px; }
  .tagline { position: absolute; top: 208px; left: 0; right: 0; text-align: center; font-size: 13px; letter-spacing: 2px; }
  .back-web { position: absolute; bottom: 40px; left: 0; right: 0; text-align: center; font-size: 14px; font-weight: 600; letter-spacing: 1px; }
</style>
</head>
<body>

<section class="card card--front" aria-label="Business card front">
  <div class="brand">
    <span class="brand__mark"></span>
    <div class="brand__name">Meridale Partners<span class="brand__sub">Pty Limited</span></div>
  </div>

  <address class="contact" style="font-style:normal">
    Corrin House<br>
    14 Fenwick Lane, Ashbury Vale 3081<br>
    <b>[t]</b> +61 3 9012 4470<br>
    <b>[f]</b> +61 3 9012 4471<br>
    <b>[e]</b> hello@meridalepartners.com<br>
    <span class="web">www.meridalepartners.com</span>
  </address>

  <div class="membership">
    <div class="membership__badge" role="img" aria-label="Member association badge"></div>
    <div class="membership__text">Member Southland Guild of Draughtsmen</div>
  </div>

  <div class="person">
    <div class="person__name">Elias Harrow <small>sgd, pmi</small></div>
    <div>Architect (SGD reg. no: 7312)</div>
    <div class="person__role">Director</div>
    <div>[m] 0412 660 238</div>
  </div>

  <div class="services-band">Architects &nbsp;•&nbsp; Urban Designers &nbsp;•&nbsp; Project Managers</div>
</section>

<section class="card card--back" aria-label="Business card back">
  <div class="brand">
    <span class="brand__mark"></span>
    <div class="brand__name">Meridale Partners<span class="brand__sub">Pty Limited</span></div>
  </div>
  <div class="tagline">Architects • Urban Designers • Project Managers</div>
  <div class="back-web">www.meridalepartners.com</div>
</section>

</body>
</html>
```